Plakate für Podologie - Medizinische Fusspflege
Zielgruppe
Podologie - Medizinische Fusspflege. Zielgruppe sind Kinder bis und mit ältere Menschen.
Aufgabenstellung
Möchte ein modernes, aber auch klassisches Design, dass Professionalität & medizinische Fundiertheit ausstrahlt. Man soll sehen, dass es medizinisch ist und nicht verwechselbar mit kosmetischer Fusspflege.

```html
<!DOCTYPE html>
<html lang="de">
<head>
<meta charset="utf-8">
<title>PediVita – Medizinische Podologie</title>
<link rel="stylesheet" href="https://fonts.googleapis.com/css2?family=Montserrat:wght@500;700;800&family=Oswald:wght@400;500;700&display=swap">
<style>
  :root {
    --forest: #0f3b31;
    --forest-text: #123a31;
    --leaf: #8ab05a;
    --vivid: #1f8a3f;
    --paper: #f3f4f5;
    --line: #7d8580;
    --white: #ffffff;
  }
  * { margin: 0; padding: 0; box-sizing: border-box; }
  html, body { width: 848px; height: 1200px; overflow: hidden; background: var(--paper); }
  .poster {
    position: relative; width: 848px; height: 1200px; overflow: hidden;
    background: var(--paper); color: var(--forest-text);
    font-family: "Montserrat", sans-serif;
  }
  .photo {
    position: absolute; left: 340px; top: 0; width: 508px; height: 960px;
    background:
      linear-gradient(to right, var(--paper) 0%, rgba(243,244,245,0.6) 22%, rgba(243,244,245,0) 45%),
      linear-gradient(160deg, #a9c6d6 0%, #c9d9e0 30%, #e4bfa6 55%, #d9a98a 75%, #a8c4d3 100%);
  }
  .brand-dot { position: absolute; left: 46px; top: 52px; width: 50px; height: 50px; border-radius: 50%; background: var(--forest); }
  .brand-name { position: absolute; left: 110px; top: 66px; font-weight: 700; font-size: 34px; color: var(--forest); line-height: 1; }
  .brand-tagline { position: absolute; left: 112px; top: 107px; font-size: 9.5px; letter-spacing: 1.6px; color: #4d5f5a; font-weight: 500; }

  .headline { position: absolute; left: 40px; top: 168px; font-family: "Oswald", sans-serif; font-weight: 700; color: var(--forest); line-height: 1; }
  .headline .line-1 { display: block; font-size: 88px; letter-spacing: -2.5px; }
  .headline .line-2 { display: block; font-size: 61px; margin-top: -6px; letter-spacing: -1.5px; }
  .headline-rule { position: absolute; left: 40px; top: 341px; width: 84px; height: 4px; background: var(--forest); }
  .intro { position: absolute; left: 42px; top: 364px; font-size: 18px; line-height: 28px; font-weight: 500; color: var(--forest-text); }

  .services { position: absolute; left: 70px; top: 434px; list-style: none; }
  .service { position: relative; width: 311px; height: 73.2px; display: flex; align-items: center; }
  .service-icon { flex-shrink: 0; width: 56px; height: 56px; border-radius: 50%; border: 2px solid var(--leaf); background: var(--paper); }
  .service-name { margin-left: 20px; font-size: 15.5px; font-weight: 800; color: var(--forest); white-space: nowrap; }
  .service::after { content: ""; position: absolute; left: 76px; right: 0; bottom: -2px; height: 1px; background: var(--line); }

  .audience { position: absolute; left: 60px; width: 340px; top: 818px; text-align: center; font-size: 19px; font-weight: 800; line-height: 30px; color: var(--forest); }

  .bands { position: absolute; left: 0; top: 0; }

  .cta {
    position: absolute; left: 502px; top: 657px; width: 252px; height: 252px; border-radius: 50%;
    background: var(--forest); border: 4px solid var(--white);
    display: flex; flex-direction: column; align-items: center; padding-top: 30px;
    font-weight: 800; line-height: 38px; text-align: center;
  }
  .cta-line { color: var(--white); font-size: 31px; }
  .cta-line.accent { color: var(--vivid); font-size: 25px; }
  .cta-icon { margin-top: 8px; }

  .contact { position: absolute; top: 957px; display: flex; gap: 14px; font-family: "Oswald", sans-serif; }
  .contact-icon { width: 55px; height: 55px; border-radius: 50%; background: var(--white); display: flex; align-items: center; justify-content: center; flex-shrink: 0; }
  .contact-label { color: var(--leaf); font-size: 22px; line-height: 30px; font-weight: 400; }
  .contact-value { color: var(--white); font-size: 21px; line-height: 29px; font-weight: 400; }
  .contact.phone { left: 31px; }
  .contact.web { left: 313px; }
  .contact.address { left: 568px; }

  .footer-rule { position: absolute; left: 31px; top: 1054px; width: 732px; height: 1px; background: rgba(255,255,255,0.55); }
  .cert { position: absolute; left: 31px; top: 1082px; }
  .cert-text { position: absolute; left: 114px; top: 1096px; font-family: "Oswald", sans-serif; color: var(--white); font-size: 26px; }
  .footer-divider { position: absolute; left: 352px; top: 1083px; width: 2px; height: 66px; background: var(--white); }
  .values { position: absolute; left: 420px; top: 1094px; font-family: "Oswald", sans-serif; color: var(--white); font-size: 28.5px; }
</style>
</head>
<body>
<div class="poster">
  <div class="photo" role="img" aria-label="Podologin hält den nackten Fuss eines Patienten in den Händen, Hintergrund in hellblauer Praxiskleidung"></div>

  <span class="brand-dot"></span>
  <span class="brand-name">PediVita</span>
  <div class="brand-tagline">MEDIZINISCHE PODOLOGIE</div>

  <h1 class="headline"><span class="line-1">IHRE FÜSSE.</span><span class="line-2">UNSERE KOMPETENZ.</span></h1>
  <div class="headline-rule"></div>
  <p class="intro">Medizinische Fussbehandlungen<br>für Ihre Gesundheit und Lebensqualität.</p>

  <ul class="services">
    <li class="service"><div class="service-icon" role="img" aria-label="Symbol Fuss"></div><div class="service-name">Medizinische Fusspflege</div></li>
    <li class="service"><div class="service-icon" role="img" aria-label="Symbol Nagelkorrektur"></div><div class="service-name">Nagelkorrektur</div></li>
    <li class="service"><div class="service-icon" role="img" aria-label="Symbol Zehennagel"></div><div class="service-name">Eingewachsene Nägel</div></li>
    <li class="service"><div class="service-icon" role="img" aria-label="Symbol Fusssohle"></div><div class="service-name">Hornhaut &amp; Hühneraugen</div></li>
    <li class="service"><div class="service-icon" role="img" aria-label="Symbol Fuss mit Tropfen"></div><div class="service-name">Diabetische Fussversorgung</div></li>
  </ul>

  <p class="audience">Auch für Risikopatienten,<br>Kinder und Sportler.</p>

  <svg class="bands" width="848" height="1200" viewBox="0 0 848 1200" aria-hidden="true">
    <path d="M0 900 C300 915 620 880 848 655 L848 1200 L0 1200 Z" fill="var(--leaf)"/>
    <path d="M0 922 C320 932 640 905 848 760 L848 1200 L0 1200 Z" fill="var(--forest)"/>
  </svg>

  <div class="cta">
    <span class="cta-line">JETZT</span>
    <span class="cta-line">TERMIN</span>
    <span class="cta-line accent">VEREINBAREN</span>
    <svg class="cta-icon" width="64" height="68" viewBox="0 0 64 68" aria-hidden="true">
      <rect x="4" y="10" width="50" height="50" rx="6" fill="none" stroke="#fff" stroke-width="5"/>
      <rect x="4" y="10" width="50" height="12" fill="#fff"/>
      <rect x="14" y="3" width="6" height="12" rx="3" fill="#fff"/>
      <rect x="38" y="3" width="6" height="12" rx="3" fill="#fff"/>
      <g fill="#fff">
        <rect x="13" y="28" width="7" height="7"/><rect x="25" y="28" width="7" height="7"/><rect x="37" y="28" width="7" height="7"/>
        <rect x="13" y="40" width="7" height="7"/><rect x="25" y="40" width="7" height="7"/>
      </g>
      <circle cx="50" cy="54" r="12" fill="#fff"/>
      <path d="M44 54 L48.5 58.5 L56 50" fill="none" stroke="var(--forest)" stroke-width="3.5" stroke-linecap="round" stroke-linejoin="round"/>
    </svg>
  </div>

  <div class="contact phone">
    <div class="contact-icon">
      <svg width="30" height="30" viewBox="0 0 24 24" aria-hidden="true"><path d="M6.6 10.8a15.1 15.1 0 0 0 6.6 6.6l2.2-2.2a1 1 0 0 1 1-.25 11.4 11.4 0 0 0 3.6.57 1 1 0 0 1 1 1V20a1 1 0 0 1-1 1A17 17 0 0 1 3 4a1 1 0 0 1 1-1h3.5a1 1 0 0 1 1 1c0 1.250.2 2.45.57 3.57a1 1 0 0 1-.25 1z" fill="var(--forest)"/></svg>
    </div>
    <div><div class="contact-label">Telefon</div><div class="contact-value">0987 / 654 321 0</div></div>
  </div>
  <div class="contact web">
    <div class="contact-icon">
      <svg width="32" height="32" viewBox="0 0 24 24" aria-hidden="true" fill="none" stroke="var(--forest)" stroke-width="1.8"><circle cx="12" cy="12" r="9"/><ellipse cx="12" cy="12" rx="4" ry="9"/><path d="M3 12h18M4.5 7.5h15M4.5 16.5h15"/></svg>
    </div>
    <div><div class="contact-label">Website</div><div class="contact-value">www.pedivita.de</div></div>
  </div>
  <div class="contact address">
    <div class="contact-icon">
      <svg width="30" height="32" viewBox="0 0 24 26" aria-hidden="true"><path d="M12 2a7 7 0 0 0-7 7c0 5 7 12 7 12s7-7 7-12a7 7 0 0 0-7-7z" fill="var(--forest)"/><circle cx="12" cy="9" r="2.6" fill="#fff"/><ellipse cx="12" cy="23" rx="7" ry="1.6" fill="var(--forest)"/></svg>
    </div>
    <div><div class="contact-label">Adresse</div><div class="contact-value">Lindenweg 7<br>54321 Talheim</div></div>
  </div>

  <div class="footer-rule"></div>
  <svg class="cert" width="58" height="66" viewBox="0 0 58 66" aria-hidden="true">
    <path d="M29 3 L54 11 V31 C54 47 43 58 29 63 C15 58 4 47 4 31 V11 Z" fill="none" stroke="var(--vivid)" stroke-width="4"/>
    <path d="M24 20 h10 v9 h9 v10 h-9 v9 h-10 v-9 h-9 v-10 h9 z" fill="var(--vivid)"/>
  </svg>
  <div class="cert-text">Zertifizierte Podologie</div>
  <div class="footer-divider"></div>
  <div class="values">Fachgerecht • Hygienisch • Modern</div>
</div>
</body>
</html>
```